Health Information/Education Logo Design

We need a logo design for a new company based in Atlanta called Brightpath Care. The program is about patient empowerment. We provide health information and education on how to get healthy, stay healthy, and how to be proactive in your care. We also provide medication and injection training to help patients feel their best and to ensure successful therapy outcomes.
We like the colors yellow, pink, teal and purple and would like to see some or all of these colors in the designs. The final design should communicate caring, considerate, compassionate information, education and training services
Education
Contact Information for Business Card
Brightpath Care
Lorraine Pettaway RN, MSN, MHA
Nurse Educator
404.555.0187 cell
404.555.0142 fax

```html
<!DOCTYPE html>
<html lang="en">
<head>
<meta charset="utf-8">
<title>Brightpath Care – Business Card</title>
<link rel="stylesheet" href="https://fonts.googleapis.com/css2?family=Andika:wght@700&family=Oswald:wght@500&family=Roboto:wght@700&display=swap">
<style>
  :root {
    --frame: #000000;
    --paper: #ffffff;
    --brand-blue: #0a12e0;
    --mark-purple: #6a1ef5;
    --name-purple: #6f22f2;
    --title-yellow: #ffff00;
    --contact-green: #33dd88;
    --stripe-sky: #4dd8ff;
    --stripe-khaki: #c0bf9b;
    --stripe-lime: #33ff00;
    --stripe-yellow: #ffff00;
    --band-blue: #0010ee;
  }
  html, body {
    margin: 0;
    padding: 0;
    width: 1200px;
    height: 625px;
    overflow: hidden;
    background: var(--paper);
  }
  .card {
    position: relative;
    width: 1200px;
    height: 625px;
    background: var(--paper);
  }
  .card-frame {
    position: absolute;
    left: 31px;
    top: 0;
    width: 1140px;
    height: 621px;
    border: 4px solid var(--frame);
    border-top-width: 2px;
    box-sizing: content-box;
    margin-left: -4px;
  }
  .brand-mark {
    position: absolute;
    left: 176px;
    top: 231px;
    width: 180px;
    height: 180px;
    border-radius: 50%;
    background: var(--mark-purple);
  }
  .brand-name {
    position: absolute;
    left: 90px;
    top: 432px;
    width: 350px;
    text-align: center;
    margin: 0;
    font-family: "Oswald", sans-serif;
    font-weight: 500;
    font-size: 46px;
    line-height: 60px;
    color: var(--brand-blue);
    text-transform: uppercase;
    letter-spacing: -0.5px;
  }
  .person {
    position: absolute;
    left: 500px;
    top: 208px;
    width: 560px;
    margin: 0;
  }
  .person-name {
    margin: 0;
    text-align: center;
    font-family: "Andika", sans-serif;
    font-weight: 700;
    font-size: 41px;
    line-height: 54px;
    color: var(--name-purple);
  }
  .person-degrees {
    position: absolute;
    left: 664px;
    top: 270px;
    margin: 0;
    font-family: "Roboto", sans-serif;
    font-weight: 700;
    font-size: 28px;
    line-height: 34px;
    color: var(--name-purple);
  }
  .person-role {
    position: absolute;
    left: 599px;
    top: 303px;
    margin: 0;
    font-family: "Roboto", sans-serif;
    font-weight: 700;
    font-size: 38px;
    line-height: 44px;
    color: var(--title-yellow);
  }
  .contact {
    position: absolute;
    left: 593px;
    top: 402px;
    margin: 0;
    padding: 0;
    list-style: none;
    font-family: "Roboto", sans-serif;
    font-weight: 700;
    font-size: 31px;
    line-height: 42px;
    color: var(--contact-green);
  }
  .contact-fax { padding-left: 8px; }
  .stripe {
    position: absolute;
    left: 31px;
    top: 541px;
    width: 1140px;
    height: 20px;
    display: flex;
  }
  .stripe span { flex: 1 1 0; }
  .stripe .sky { background: var(--stripe-sky); flex-basis: 271px; flex-grow: 0; }
  .stripe .khaki { background: var(--stripe-khaki); flex-basis: 270px; flex-grow: 0; }
  .stripe .lime { background: var(--stripe-lime); flex-basis: 269px; flex-grow: 0; }
  .stripe .yellow { background: var(--stripe-yellow); }
  .base-band {
    position: absolute;
    left: 31px;
    top: 561px;
    width: 1140px;
    height: 47px;
    background: var(--band-blue);
  }
</style>
</head>
<body>
  <main class="card">
    <div class="card-frame"></div>

    <div class="brand-mark" aria-hidden="true"></div>
    <p class="brand-name">Brightpath Care</p>

    <div class="person">
      <h1 class="person-name">Lorraine Pettaway,RN</h1>
    </div>
    <p class="person-degrees">MSN, MHA</p>
    <p class="person-role">Nurse Educator</p>

    <ul class="contact">
      <li class="contact-cell">Cell : 404.555.0187</li>
      <li class="contact-fax">Fax : 404.555.0142</li>
    </ul>

    <div class="stripe" aria-hidden="true">
      <span class="sky"></span>
      <span class="khaki"></span>
      <span class="lime"></span>
      <span class="yellow"></span>
    </div>
    <div class="base-band" aria-hidden="true"></div>
  </main>
</body>
</html>
```